Health Benefits Association Website Design

The Allied Household Provision Association (AHPA) is an organization formed for the purpose of providing its members better value for selected health benefits and services. Members can use the association benefits either in conjunction with or independently of other medical insurance they may have. Some of the benefits available include discounted dental and vision care and prescription mail order services. There is no limitation on who can join. This membership will be primarily marketed as a way to enhance the value of a fixed benefit health insurance plan although members do not have to have the insurance plan join the association.

We are seeking a design for a website to be used for consumers to get information about membership and for current members to be able to access their benefits. The website should include:

1) A landing page to provide a description of the AHPA

2) A secondary page that can be duplicated that will:
a. Provide a list of benefits
b. Provide a membership enrollment form
c. Provide a member’s only access page
d. Provide a contact page for more information

We are seeking a modern but conservative design that will reflect value, simplicity and good health. The site design will also need to be compatible for use with mobile phones and tablets.

A copy of the association logo is included with the submission. It will also need to be incorporated into the website design. Layouts of similar association websites have also been included for reference.

Target Market(s)

Ages 25 to 65 unmarried, married with no children, professionals, self-employed, active and healthy

Industry/Entity Type

Health And Wellness

Number of Pages Required

2 page

Font styles to use
Sans Serif

Colors

Designer to choose colors to be used in the design.

Requirements
Must have
• AHPA Logo (attached). Use colors from the logo in the website design.
Nice to have
• Graphics, if used, should convey health and fitness and skew toward a diverse array of adults 25 to 40.

```html
<!DOCTYPE html>
<html lang="en">
<head>
<meta charset="utf-8">
<title>Allied Household Provision Association</title>
<link rel="stylesheet" href="https://fonts.googleapis.com/css2?family=Bitter:wght@400;500&family=Mulish:wght@400;600&display=swap">
<style>
:root{
  --olive:#939b52;
  --olive-dark:#7d8540;
  --yellow:#fccb0d;
  --pale-yellow:#fbd97a;
  --ink:#222;
  --body:#444;
  --footer:#ebebee;
  --rule:#d3d3d6;
  --social:#7aa0b8;
  --social-hot:#ef6a4f;
  --white:#fff;
}
*{margin:0;padding:0;box-sizing:border-box}
html,body{width:1200px;height:2187px;overflow:hidden;background:var(--white)}
body{position:relative;font-family:"Mulish",sans-serif;color:var(--body)}
.abs{position:absolute}
/* header */
.header-line{left:0;top:122px;width:1200px;height:2px;background:var(--yellow)}
.brand{left:493px;top:12px;width:217px;height:180px;background:var(--white);display:flex;flex-direction:column;align-items:center;justify-content:center;gap:6px;text-align:center}
.brand-dot{width:22px;height:22px;border-radius:50%;background:var(--yellow)}
.brand-name{font-family:"Bitter",serif;font-weight:500;color:var(--olive);font-size:20px;line-height:1.15}
.call{left:943px;top:34px;font-family:"Bitter",serif;font-size:14px;color:var(--ink)}
.phone{left:910px;top:58px;display:flex;align-items:center;gap:10px;font-family:"Bitter",serif;font-size:21px;color:var(--olive)}
.nav a{position:absolute;top:124px;height:73px;line-height:73px;font-family:"Bitter",serif;font-size:14px;color:var(--ink);text-decoration:none}
.nav a.active{background:var(--yellow);padding:0 14px;font-weight:500}
/* hero */
.hero{left:0;top:197px;width:1200px;height:568px;background:linear-gradient(100deg,#4f5a25 0%,#6f7a32 35%,#8a8a3a 60%,#5a5e28 100%)}
.hero-figure{left:720px;top:197px;width:340px;height:568px;background:linear-gradient(180deg,#b0466e 0%,#d13d88 45%,#2b2b2b 100%);border-radius:160px 160px 0 0;opacity:.55}
.hero-panel{left:178px;top:383px;width:427px;height:244px;background:rgba(20,20,10,.72)}
.hero-title{left:216px;top:400px;font-family:"Bitter",serif;font-size:56px;line-height:60px;color:var(--white);font-weight:400}
.btn{display:flex;align-items:center;justify-content:center;gap:12px;background:var(--yellow);font-family:"Bitter",serif;color:var(--ink);text-decoration:none}
.hero-btn{left:219px;top:539px;width:178px;height:56px;font-size:19px}
.dots{left:549px;top:713px;display:flex;gap:12px}
.dots span{width:9px;height:9px;border-radius:50%;background:var(--white)}
.dots span.on{background:var(--yellow)}
/* welcome */
.section-mark{left:0;top:850px;width:1200px;text-align:center;font-family:"Bitter",serif;font-weight:500;font-size:20px;color:var(--olive)}
.section-mark-rule{left:505px;top:925px;width:190px;height:5px;background:var(--olive)}
.heading{left:0;width:1200px;text-align:center;font-family:"Bitter",serif;font-weight:400;font-size:32px;color:var(--olive)}
.intro{left:300px;top:1024px;width:600px;text-align:center;font-size:14.5px;line-height:24px;color:var(--body)}
.intro p+p{margin-top:24px}
.intro-btn{left:526px;top:1204px;width:158px;height:44px;font-size:15px}
.intro-btn-rule{left:526px;top:1250px;width:158px;height:2px;background:var(--yellow)}
.divider{left:379px;top:1339px;width:452px;height:14px;border-radius:7px;background:linear-gradient(90deg,rgba(147,155,82,.15) 0%,var(--pale-yellow) 20%,#fde7a8 50%,var(--pale-yellow) 80%,rgba(147,155,82,.15) 100%)}
/* benefits */
.card{top:1531px;width:238px;height:245px;background:var(--white);box-shadow:0 2px 10px rgba(0,0,0,.14);display:flex;flex-direction:column;align-items:center;padding-top:50px}
.card-title{font-family:"Bitter",serif;font-size:20px;color:var(--olive);margin-top:34px}
.card.active{background:var(--olive);padding-top:22px}
.card.active .card-title{color:var(--white);margin-top:10px}
.card-text{color:var(--white);font-size:12.5px;line-height:18px;text-align:center;width:170px;margin-top:14px}
.card-rule{left:359px;top:1779px;width:237px;height:5px;background:var(--olive)}
.consumer-icon{width:80px;height:80px;border-radius:50%;background:#c9cc98}
/* footer */
.footer{left:0;top:1863px;width:1200px;height:324px;background:var(--footer);border-top:2px solid var(--rule)}
.foot-brand{left:125px;top:1950px;width:150px;display:flex;flex-direction:column;align-items:center;gap:8px;text-align:center}
.foot-brand .brand-name{font-size:17px}
.foot-brand .brand-dot{width:18px;height:18px}
.vrule{top:1929px;width:1px;height:175px;background:var(--rule)}
.foot-label{font-family:"Bitter",serif;font-size:11.5px;font-weight:500;color:var(--ink);letter-spacing:.5px}
.foot-links{left:367px;top:1967px;font-size:11px;color:#333}
.foot-links span{margin:0 6px;color:#999}
.foot-contact{left:367px;top:2063px;font-size:11px;line-height:24px;color:#333}
.foot-contact span{margin:0 6px;color:#999}
.social{left:878px;top:1980px;display:flex;gap:23px}
.social a{width:32px;height:32px;border-radius:50%;border:1.5px solid var(--social);display:flex;align-items:center;justify-content:center}
.social a i{width:10px;height:10px;background:var(--social);border-radius:2px}
.social a.hot{background:var(--social-hot);border-color:var(--social-hot)}
.social a.hot i{background:var(--white)}
.copyright{left:876px;top:2096px;font-size:11px;color:#333}
</style>
</head>
<body>

<header>
  <div class="abs header-line"></div>
  <div class="abs brand">
    <span class="brand-dot"></span>
    <span class="brand-name">Allied Household<br>Provision<br>Association</span>
  </div>
  <div class="abs call">Call us On</div>
  <div class="abs phone">
    <svg width="18" height="18" viewBox="0 0 24 24" aria-hidden="true"><path fill="#939b52" d="M6.6 10.8a15 15 0 0 0 6.6 6.6l2.2-2.2a1 1 0 0 1 1-.25 11.4 11.4 0 0 0 3.6.57 1 1 0 0 1 1 1V20a1 1 0 0 1-1 1A17 17 0 0 1 3 4a1 1 0 0 1 1-1h3.5a1 1 0 0 1 1 1c0 1.25.2 2.45.57 3.57a1 1 0 0 1-.25 1z"/></svg>
    555.010.4821
  </div>
  <nav class="nav">
    <a class="active" href="#" style="left:172px">Home</a>
    <a href="#" style="left:266px">News</a>
    <a href="#" style="left:335px">Charities</a>
    <a href="#" style="left:429px">Benefits</a>
    <a href="#" style="left:716px">Enroll</a>
    <a href="#" style="left:810px">Members area</a>
    <a href="#" style="left:946px">Contact&nbsp; Us</a>
  </nav>
</header>

<section>
  <div class="abs hero" role="img" aria-label="Photo of a smiling woman in a pink running shirt jogging through a sunlit forest"></div>
  <div class="abs hero-figure" aria-hidden="true"></div>
  <div class="abs hero-panel"></div>
  <h1 class="abs hero-title">Better Health<br>Services</h1>
  <a class="abs btn hero-btn" href="#">READ MORE
    <svg width="8" height="10" viewBox="0 0 8 10" aria-hidden="true"><path d="M0 0l8 5-8 5z" fill="#222"/></svg></a>
  <div class="abs dots"><span></span><span class="on"></span><span></span><span></span><span></span></div>
</section>

<section>
  <div class="abs section-mark">Allied Household Provision Association</div>
  <div class="abs section-mark-rule"></div>
  <h2 class="abs heading" style="top:958px">Welcome to our site</h2>
  <div class="abs intro">
    <p>Welcome to the Allied Household Provision Association (AHPA). AHPA was started to be part of a senior-focused charitable organization that is different from other organizations with a similar perspective or mission.</p>
    <p>AHPA believes a charity should focus on raising money to support its mission, not its leaders. So, none of the AHPA officers or board members receive any compensation.</p>
  </div>
  <a class="abs btn intro-btn" href="#">READ MORE
    <svg width="7" height="9" viewBox="0 0 8 10" aria-hidden="true"><path d="M0 0l8 5-8 5z" fill="#222"/></svg></a>
  <div class="abs intro-btn-rule"></div>
  <div class="abs divider" role="img" aria-label="Decorative divider ornament with tapered lines, dots and a row of stars"></div>
</section>

<section>
  <h2 class="abs heading" style="top:1428px">Our Benefits</h2>

  <div class="abs card" style="left:105px">
    <svg width="92" height="76" viewBox="0 0 92 76" aria-hidden="true">
      <path d="M46 74 C10 48 6 34 10 20 C15 4 36 2 46 18 C56 2 77 4 82 20 C86 34 82 48 46 74Z" fill="#939b52"/>
      <path d="M0 42 H30 L36 28 L44 56 L50 38 H64" stroke="#fbd97a" stroke-width="5" fill="none" stroke-linejoin="round"/>
    </svg>
    <div class="card-title">Health</div>
  </div>

  <div class="abs card active" style="left:359px">
    <div class="consumer-icon" role="img" aria-label="Consumer icon"></div>
    <div class="card-title">Consumer</div>
    <div class="card-text">Welcome to the Allied Household Provision Association (AHPA). AHPA was started to be par</div>
  </div>
  <div class="abs card-rule"></div>

  <div class="abs card" style="left:612px">
    <svg width="60" height="80" viewBox="0 0 60 80" aria-hidden="true">
      <path d="M30 2 C12 2 2 16 4 32 C6 46 18 54 22 62 H38 C42 54 54 46 56 32 C58 16 48 2 30 2Z" fill="#939b52"/>
      <path d="M30 2 C22 12 22 50 26 62 H34 C38 50 38 12 30 2Z" fill="#fbd97a"/>
      <rect x="22" y="66" width="16" height="10" rx="2" fill="#939b52"/>
    </svg>
    <div class="card-title">Travel</div>
  </div>

  <div class="abs card" style="left:866px">
    <svg width="66" height="78" viewBox="0 0 66 78" aria-hidden="true">
      <rect x="22" y="2" width="22" height="10" rx="3" fill="none" stroke="#939b52" stroke-width="4"/>
      <rect x="2" y="12" width="62" height="62" rx="6" fill="#939b52"/>
      <rect x="10" y="26" width="46" height="4" fill="#fbd97a"/>
      <rect x="10" y="36" width="46" height="4" fill="#fbd97a"/>
      <rect x="10" y="46" width="46" height="4" fill="#fbd97a"/>
      <rect x="10" y="56" width="46" height="4" fill="#fbd97a"/>
    </svg>
    <div class="card-title">Business</div>
  </div>
</section>

<footer>
  <div class="abs footer"></div>
  <div class="abs foot-brand">
    <span class="brand-dot"></span>
    <span class="brand-name">Allied Household<br>Provision<br>Association</span>
  </div>
  <div class="abs vrule" style="left:315px"></div>
  <div class="abs vrule" style="left:825px"></div>

  <div class="abs foot-label" style="left:367px;top:1942px">MENU</div>
  <div class="abs foot-links">Home<span>|</span>News<span>|</span>Charities<span>|</span>Benefits<span>|</span>Enroll<span>|</span>Memnbers Area<span>|</span>Contact us</div>

  <div class="abs foot-label" style="left:367px;top:2029px">CONTACT US</div>
  <div class="abs foot-contact">218 Linden Court<span>|</span>Harwell, OR 97031<br>T : 555.014.2290<span>|</span>E : info@ahpa-members.org</div>

  <div class="abs foot-label" style="left:884px;top:1942px">FOLLOW US ON</div>
  <nav class="abs social" aria-label="Social links">
    <a href="#" aria-label="Social network one"><i></i></a>
    <a href="#" aria-label="Social network two"><i></i></a>
    <a href="#" class="hot" aria-label="Social network three"><i></i></a>
    <a href="#" aria-label="Social network four"><i></i></a>
  </nav>
  <div class="abs copyright">Copyrights @ 2017 All Rights Reserved</div>
</footer>

</body>
</html>
```